Business Card Design Project

KRV Management Consulting, LLC is a management consulting firm focused on improving an organization’s health and wellness while enhancing company performance with an emphasis on winning in the marketplace, profitable growth, team building, culture enablement and innovation.

Industry/Entity Type

Business

```html
<!DOCTYPE html>
<html lang="en">
<head>
<meta charset="utf-8">
<title>KRV Management Consulting, LLC — Business Card</title>
<link rel="stylesheet" href="https://fonts.googleapis.com/css2?family=Libre+Baskerville&family=PT+Sans&display=swap">
<style>
  :root {
    --page-bg: #ffffff;
    --card-bg: #222222;
    --text-light: #ffffff;
    --accent-green: #7dbb3c;
  }
  html, body {
    margin: 0;
    padding: 0;
    width: 1200px;
    height: 720px;
    overflow: hidden;
    background: var(--page-bg);
  }
  .canvas {
    position: relative;
    width: 1200px;
    height: 720px;
  }
  .business-card {
    position: absolute;
    left: 36px;
    top: 38px;
    width: 1125px;
    height: 642px;
    background: var(--card-bg);
    border-radius: 64px;
    overflow: hidden;
  }
  .brand {
    position: absolute;
    left: 40px;
    top: 242px;
  }
  .brand-name {
    margin: 0;
    font-family: "Libre Baskerville", "Times New Roman", serif;
    font-weight: 400;
    font-size: 78px;
    line-height: 1;
    letter-spacing: -2px;
    color: var(--text-light);
  }
  .brand-tagline {
    margin: 6px 0 0 2px;
    font-family: "PT Sans", Arial, sans-serif;
    font-size: 32px;
    line-height: 1;
    letter-spacing: 0.3px;
    color: var(--text-light);
  }
  .accent-rule {
    position: absolute;
    left: 657px;
    top: 319px;
    width: 468px;
    height: 6px;
    background: var(--accent-green);
  }
</style>
</head>
<body>
  <main class="canvas">
    <section class="business-card" aria-label="KRV Management Consulting business card">
      <div class="brand">
        <h1 class="brand-name">KRV</h1>
        <p class="brand-tagline">Management Consulting, LLC</p>
      </div>
      <div class="accent-rule" aria-hidden="true"></div>
    </section>
  </main>
</body>
</html>
```